new letterhead for my brokergae company KeelBright, Complete Marine Brokerage

We need a new letterhead for our brokerage company called KeelBright. We are specialised in selling pleasure crafts (sailing and motoryachts). More info can be found at https://keelbright-example.com/en

I use this document for a quotation, a letter, sales agreement, selling instructions. I am looking for a cover page + a content page.

Th efollowing information needs to be in the header / footer; email, website, VAT number, Bank Account number, number chamber of ccomerce, registry number prav, General terms and conditions DQRT apply.

```html
<!DOCTYPE html>
<html lang="en">
<head>
<meta charset="utf-8">
<title>KeelBright Letterhead – Cover and Content Page</title>
<link rel="stylesheet" href="https://fonts.googleapis.com/css2?family=Open+Sans:wght@400;600;700&family=PT+Sans+Narrow:wght@400;700&display=swap">
<style>
  :root {
    --backdrop: #7fb1e3;
    --paper: #ffffff;
    --navy: #1f4f9c;
    --brand-blue: #1c5aa8;
    --orange: #f0562a;
    --ink: #3b3f46;
    --rule: #9aa3ad;
    --tab: #e4e6ea;
    --tint: #e6eefb;
  }
  * { box-sizing: border-box; margin: 0; padding: 0; }
  html, body { width: 1200px; height: 784px; overflow: hidden; }
  body {
    background: var(--backdrop);
    display: flex; align-items: center; justify-content: center; gap: 40px;
    font-family: "PT Sans Narrow", "Arial Narrow", sans-serif;
  }
  .letterhead {
    position: relative;
    width: 500px; height: 708px;
    background: linear-gradient(to top, var(--tint) 0%, var(--paper) 22%);
    box-shadow: 0 2px 8px rgba(20, 60, 120, .25);
    overflow: hidden;
  }
  .corner-mark { position: absolute; display: flex; gap: 3px; }
  .corner-mark span { display: block; }
  .corner-mark--top { top: 0; left: 10px; }
  .corner-mark--top span { width: 22px; height: 4px; }
  .corner-mark--side { right: 0; top: 10px; flex-direction: column; }
  .corner-mark--side span { width: 4px; height: 22px; }
  .mark-orange { background: var(--orange); }
  .mark-navy { background: var(--navy); }

  .brand { position: absolute; top: 66px; right: 42px; }
  .brand__name {
    font-family: "Open Sans", sans-serif; font-weight: 600;
    font-size: 29px; color: var(--brand-blue); letter-spacing: -.3px; line-height: 1;
  }
  .brand__tagline {
    font-family: "Open Sans", sans-serif; font-weight: 600;
    font-size: 6.2px; letter-spacing: 2.2px; color: var(--brand-blue);
    text-transform: uppercase; margin-top: 5px; text-align: right;
  }
  .letterhead--content .brand { top: 40px; }
  .letterhead--content .brand__name { font-size: 22px; }
  .letterhead--content .brand__tagline { font-size: 5.2px; letter-spacing: 1.8px; }

  .footer { position: absolute; left: 0; right: 0; bottom: 0; height: 96px; }
  .footer__rule { position: absolute; left: 38px; right: 0; top: 0; border-top: 1px solid var(--rule); }
  .footer__tab {
    position: absolute; top: -6px; height: 12px; padding: 0 6px;
    background: var(--tab); font-weight: 700; font-size: 7px; line-height: 12px; color: var(--ink);
    border-left: 2px solid var(--orange); border-right: 2px solid var(--navy);
  }
  .footer__tab--contact { left: 100px; }
  .footer__tab--general { left: 250px; }
  .footer__lines {
    position: absolute; top: 14px; left: 20px; right: 12px;
    display: flex; flex-direction: column; gap: 7px;
  }
  .footer__line {
    font-size: 7.5px; line-height: 9px; color: var(--ink); white-space: nowrap;
    display: flex; align-items: center; gap: 4px;
  }
  .footer__line--contact { padding-left: 34px; }
  .footer__line--terms { padding-left: 34px; font-weight: 700; }
  .dot { width: 6px; height: 6px; border-radius: 50%; display: inline-block; flex: none; border: 1.5px solid #fff; box-shadow: 0 0 0 .5px currentColor; }
  .dot--navy { background: var(--navy); color: var(--navy); }
  .dot--orange { background: var(--orange); color: var(--orange); }
  .footer__band { position: absolute; left: 0; right: 0; bottom: 0; height: 11px; display: flex; gap: 2px; background: #fff; }
  .band-orange { background: linear-gradient(to bottom, #f57548, var(--orange)); }
  .band-navy { background: linear-gradient(to bottom, #3c6fb8, var(--navy)); }
  .band-first { flex: 0 0 26%; }
  .band-middle { flex: 0 0 34%; }
  .band-last { flex: 1; }
</style>
</head>
<body>
  <main class="letterhead letterhead--cover">
    <div class="corner-mark corner-mark--top"><span class="mark-orange"></span><span class="mark-navy"></span></div>
    <div class="corner-mark corner-mark--side"><span class="mark-navy"></span><span class="mark-orange"></span></div>

    <header class="brand">
      <div class="brand__name">KeelBright</div>
      <div class="brand__tagline">Complete Marine Brokerage</div>
    </header>

    <footer class="footer">
      <div class="footer__rule"></div>
      <div class="footer__tab footer__tab--contact">Contact Details:</div>
      <div class="footer__tab footer__tab--general">General Information:</div>
      <div class="footer__lines">
        <p class="footer__line footer__line--contact">
          <span class="dot dot--navy"></span>Harbourweg 12, 1234 AB Havenstad
          <span class="dot dot--navy"></span>+31 (0)20 555 01 23
          <span class="dot dot--navy"></span>contact@keelbright-example.com
          <span class="dot dot--navy"></span>www.keelbright-example.com
        </p>
        <p class="footer__line footer__line--general">
          <span class="dot dot--orange"></span>VAT Number: 123456789
          <span class="dot dot--orange"></span>Bank Account Number: 123456789
          <span class="dot dot--orange"></span>Number Chamber of commerce: 123456789
          <span class="dot dot--orange"></span>Registry number PRAV: 123456789
        </p>
        <p class="footer__line footer__line--terms">General terms and conditions DQRT apply</p>
      </div>
      <div class="footer__band">
        <span class="band-orange band-first"></span>
        <span class="band-navy band-middle"></span>
        <span class="band-orange band-last"></span>
      </div>
    </footer>
  </main>

  <main class="letterhead letterhead--content">
    <div class="corner-mark corner-mark--top"><span class="mark-orange"></span><span class="mark-navy"></span></div>
    <div class="corner-mark corner-mark--side"><span class="mark-navy"></span><span class="mark-orange"></span></div>

    <header class="brand">
      <div class="brand__name">KeelBright</div>
      <div class="brand__tagline">Complete Marine Brokerage</div>
    </header>

    <footer class="footer">
      <div class="footer__rule"></div>
      <div class="footer__tab footer__tab--contact">Contact Details:</div>
      <div class="footer__tab footer__tab--general">General Information:</div>
      <div class="footer__lines">
        <p class="footer__line footer__line--contact">
          <span class="dot dot--navy"></span>Harbourweg 12, 1234 AB Havenstad
          <span class="dot dot--navy"></span>+31 (0)20 555 01 23
          <span class="dot dot--navy"></span>contact@keelbright-example.com
          <span class="dot dot--navy"></span>www.keelbright-example.com
        </p>
        <p class="footer__line footer__line--general">
          <span class="dot dot--orange"></span>VAT Number: 123456789
          <span class="dot dot--orange"></span>Bank Account Number: 123456789
          <span class="dot dot--orange"></span>Number Chamber of commerce: 123456789
          <span class="dot dot--orange"></span>Registry number PRAV: 123456789
        </p>
        <p class="footer__line footer__line--terms">General terms and conditions DQRT apply</p>
      </div>
      <div class="footer__band">
        <span class="band-orange band-first"></span>
        <span class="band-navy band-middle"></span>
        <span class="band-orange band-last"></span>
      </div>
    </footer>
  </main>
</body>
</html>
```